Need a business card design for a residential architect.

You can get a sense of his work at www.tbrolvik.com

Would like a consistent look and feel between business card and website
.

Target Market(s)

Residential homeowners builders

Industry/Entity Type

Residential

Contact Information for Business Card

Dale Brolvik
Principle
Brolvik Architecture
418 Quill Lane
Menlo Park, CA 94025

dale@tbrolvik.com

tbrolvik.com
phone: 650-555-0172
Fax: 650-555-0196

Font styles to use
Sans Serif

Requirements
Must have
• Details above
Nice to have
• Would like a consistent look and feel between business card and website
Should not have
• None

```html
<!DOCTYPE html>
<html lang="en">
<head>
<meta charset="utf-8">
<title>Brolvik Architecture – Business Card</title>
<link href="https://fonts.googleapis.com/css2?family=Open+Sans:wght@400;600;700&display=swap" rel="stylesheet">
<style>
  :root {
    --bg: #ececec;
    --card: #f7f7f7;
    --band: #8c8c8c;
    --ink: #6e6e6e;
    --ink-dark: #3c3c3c;
    --white: #ffffff;
  }
  * { box-sizing: border-box; margin: 0; padding: 0; }
  html, body { width: 1200px; height: 1001px; overflow: hidden; }
  body {
    background: var(--bg);
    font-family: "Open Sans", Arial, sans-serif;
    position: relative;
  }
  .card {
    position: absolute;
    width: 525px;
    height: 300px;
    background: var(--card);
    box-shadow: 0 6px 18px rgba(0,0,0,0.12);
    overflow: hidden;
  }
  .card--info { left: 45px; top: 350px; }
  .card--brand { left: 630px; top: 350px; }

  .wordmark {
    color: var(--ink);
    font-weight: 600;
    letter-spacing: 0.5px;
    white-space: nowrap;
  }
  .card--info .wordmark {
    position: absolute;
    right: 40px;
    top: 36px;
    font-size: 26px;
  }
  .card--brand .wordmark {
    position: absolute;
    left: 0; right: 0;
    top: 112px;
    text-align: center;
    font-size: 34px;
  }

  .person {
    position: absolute;
    left: 40px;
    top: 118px;
    width: 180px;
    text-align: right;
    color: var(--ink);
  }
  .person__name { font-size: 18px; font-weight: 700; }
  .person__role { font-size: 13px; margin-top: 2px; }

  .contact {
    position: absolute;
    left: 250px;
    top: 118px;
    list-style: none;
    color: var(--ink-dark);
    font-size: 14px;
    line-height: 22px;
  }
  .contact li { display: flex; align-items: center; gap: 8px; }
  .contact svg { width: 13px; height: 13px; fill: var(--ink); flex: none; }

  .band {
    position: absolute;
    left: 0; right: 0; bottom: 0;
    height: 14px;
    background: var(--band);
  }
  .card--brand .band { height: 12px; }
  .web-tab {
    position: absolute;
    right: 0;
    bottom: 0;
    width: 290px;
    height: 50px;
    background: var(--band);
    border-top-left-radius: 16px;
    color: var(--white);
    font-size: 18px;
    font-weight: 700;
    display: flex;
    align-items: center;
    justify-content: center;
    letter-spacing: 0.3px;
  }
</style>
</head>
<body>

<section class="card card--info">
  <div class="wordmark">Brolvik Architecture</div>

  <div class="person">
    <div class="person__name">Dale Brolvik</div>
    <div class="person__role">Principle</div>
  </div>

  <ul class="contact">
    <li>
      <svg viewBox="0 0 24 24" aria-hidden="true"><path d="M12 2a7 7 0 0 0-7 7c0 5 7 13 7 13s7-8 7-13a7 7 0 0 0-7-7zm0 9.5A2.5 2.5 0 1 1 12 6.5a2.5 2.5 0 0 1 0 5z"/></svg>
      418 Quill Lane Menlo Park, CA 94025
    </li>
    <li>
      <svg viewBox="0 0 24 24" aria-hidden="true"><path d="M2 5h20v14H2zm2 2v.5l8 5.5 8-5.5V7l-8 5.5z"/></svg>
      dale@tbrolvik.com
    </li>
    <li>
      <svg viewBox="0 0 24 24" aria-hidden="true"><path d="M6.6 10.8a15 15 0 0 0 6.6 6.6l2.2-2.2c.3-.3.7-.4 1-.2 1.1.4 2.3.6 3.6.6.6 0 1 .4 1 1V20c0 .6-.4 1-1 1A17 17 0 0 1 3 4c0-.6.4-1 1-1h3.5c.6 0 1 .4 1 1 0 1.3.2 2.5.6 3.6.1.3 0 .7-.2 1z"/></svg>
      650-555-0172
    </li>
    <li>
      <svg viewBox="0 0 24 24" aria-hidden="true"><path d="M6 3h10v5H6zM4 9h16a2 2 0 0 1 2 2v6h-4v4H6v-4H2v-6a2 2 0 0 1 2-2zm4 7v3h8v-3z"/></svg>
      650-555-0196
    </li>
  </ul>

  <div class="band"></div>
  <div class="web-tab">www.tbrolvik.com</div>
</section>

<section class="card card--brand">
  <div class="wordmark">Brolvik Architecture</div>
  <div class="band"></div>
</section>

</body>
</html>
```